Web Site for Strategy and Technology Consulting Company

We are looking for a website design that engages potential customers to understand our services and contact us. In this contest, we are looking for a homepage design, but the winning designer will be favored for the design of some of the more complicated interior pages of the site. An additional contest (or contests) for these pages will be added soon.

PLATROM AND RESPONSIVE DESIGN
The site will be implemented in WordPress using the Elementor page builder.
We are looking for a design that will look good on phones are well as laptop browsers.

UPLOADED FILES INCLUDE:
1a A wireframe of the homepage we are looking for. The Uploaded PDF also includes a draft of the text proposed for the homepage. Designers are free to go beyond the wireframe, but all elements of the wireframe should be included.
1b A Word document with the draft text of the homepage.
2a-d The Norvalith logo. Two versions are included – a dark version which works well against a light background, and a light version which works well against a dark background.
3 The Norvalith color palette with HEX and RGB values. Designers are not limited to this palette, but colors should be complementary.
4 A draft of the homepage menu
5 Service sheets with information on the services we provide

MORE ABOUT NORVALITH
Norvalith is a consulting company focused on transforming businesses through software. Our tagline, “Transformation Delivered,” recognizes the gap business often have between business transformation and the software they end up with. By listening to our customers and understanding their vision and where they are, we help get our customers where they want to go.

We increase our capability by working with many consultants and partners, allowing us to provide our customers with the best people and the software that best suits them.

Industry/Entity Type

Consulting

Number of Pages Required

1 page

Font styles to use
Sans Serif

Requirements
Must have
• the content represented on the wireframe uploaded
Nice to have
• interactive features, such as roll-over icons that reveal additional information

```html
<!DOCTYPE html>
<html lang="en">
<head>
<meta charset="utf-8">
<title>Norvalith — Transformation Delivered</title>
<link href="https://fonts.googleapis.com/css2?family=Inter:ital,wght@0,400;0,500;0,600;0,700;0,800;1,400&display=swap" rel="stylesheet">
<style>
:root{
  --navy:#0d4a72;
  --blue:#1f5f96;
  --yellow:#e3b90f;
  --ink:#3b4a5a;
  --card:#e4ebf3;
  --pale:#f5f8fc;
  --footer:#2c3d55;
  --white:#ffffff;
}
*{box-sizing:border-box;margin:0;padding:0}
html,body{width:1200px;height:3010px;overflow:hidden;font-family:"Inter",sans-serif;color:var(--ink);background:var(--white)}
.wrap{position:relative;width:1200px;height:3010px}
.y{color:var(--yellow)}
/* header */
.site-header{height:80px;display:flex;align-items:center;justify-content:space-between;padding:0 94px}
.brand{display:flex;align-items:center;gap:8px;font-size:38px;font-weight:500;color:#5d6670;letter-spacing:-.5px}
.brand-dot{width:12px;height:12px;background:var(--blue);border-radius:50%}
.nav{display:flex;align-items:center;gap:36px;font-size:14px;font-weight:500;color:var(--navy)}
.nav span::after{content:"";display:inline-block;width:6px;height:6px;border-right:2px solid var(--navy);border-bottom:2px solid var(--navy);transform:rotate(45deg);margin-left:10px;position:relative;top:-3px}
.btn-contact{background:var(--blue);color:#fff;padding:11px 14px;font-size:14px;font-weight:600}
/* hero */
.hero{position:relative;height:643px;overflow:hidden}
.hero-photo{position:absolute;inset:0;background:linear-gradient(90deg,#0d4a72 0%,#12507a 45%,#3b6f94 70%,#8aa5b8 100%)}
.hero-body{position:relative;padding:100px 0 0 94px;width:760px;color:#fff}
.hero h1{font-size:55px;font-weight:800;letter-spacing:-1px;line-height:1;white-space:nowrap}
.hero p{font-size:13.5px;line-height:20px;margin-top:20px;width:650px}
.ticks{list-style:none;margin-top:22px;width:480px}
.ticks li{position:relative;padding-left:26px;font-size:13.5px;line-height:20px;margin-bottom:13px}
.ticks li::before{content:"";position:absolute;left:0;top:4px;width:8px;height:8px;background:var(--yellow);box-shadow:4px -4px 0 -1px var(--yellow)}
.btn-y{display:inline-block;background:var(--yellow);color:var(--navy);font-weight:700;font-size:15px;padding:16px 27px;letter-spacing:.3px}
/* tech services */
.services{padding:95px 94px 0}
.services-top{display:flex;justify-content:space-between;align-items:flex-start}
h2{font-size:35px;font-weight:700;color:var(--navy);letter-spacing:-.5px}
.services-top p{font-size:13.5px;line-height:20px;margin-top:16px;width:640px}
.btn-b{background:var(--blue);color:#fff;font-weight:700;font-size:15px;padding:16px 27px;margin-top:30px}
.cards{display:flex;gap:14px;margin-top:53px}
.card{width:192px;height:195px;background:var(--card);border:1px solid #cfd9e4;padding:20px;display:flex;flex-direction:column;justify-content:space-between}
.card-icon{width:64px;height:64px;border:4px solid var(--navy);border-radius:8px;position:relative}
.card-icon::after{content:"";position:absolute;right:8px;bottom:8px;width:16px;height:16px;background:var(--yellow)}
.card h3{font-size:17px;font-weight:700;color:var(--navy);line-height:27px}
.card.active{background:var(--navy);color:#fff;justify-content:flex-start}
.card.active h3{font-size:14px;color:#fff;line-height:18px}
.card.active p{font-size:11.5px;line-height:20px;margin-top:20px}
.card.active .learn{background:var(--yellow);color:var(--navy);font-size:13px;font-weight:600;text-align:center;padding:8px 0;margin-top:14px}
/* people */
.people{position:absolute;top:1271px;left:0;width:1200px;height:530px;background:var(--navy);display:flex}
.people-photo{width:500px;height:530px;background:linear-gradient(160deg,#9aa6ad,#6d6157 60%,#8b6a48)}
.people-body{padding:80px 0 0 113px;width:600px;color:#fff}
.people-body h2{color:#fff}
.people-body p{font-size:13.5px;line-height:20px;margin-top:18px}
.people-body .ticks{width:auto}
/* testimonials */
.clients{position:absolute;top:1801px;left:0;width:1200px;height:560px;background:var(--pale);padding:80px 94px 0}
.clients-top{display:flex;justify-content:space-between;align-items:center;border-bottom:1px solid #e1e7ee;padding-bottom:22px}
.arrows{display:flex;gap:14px}
.arrow{width:40px;height:40px;border:1px solid #8da0b4;display:flex;align-items:center;justify-content:center}
.arrow.on{background:#8da0b4}
.quotes{display:flex;gap:27px;margin-top:40px}
.quote{position:relative;width:320px;height:287px;background:#fff;box-shadow:0 4px 12px rgba(20,50,80,.06);padding:70px 26px 0}
.quote::before{content:"";position:absolute;left:0;right:0;top:25px;height:3px;background:var(--blue)}
.qmark{position:absolute;right:26px;top:0;width:54px;height:54px;background:#fff;box-shadow:0 2px 6px rgba(0,0,0,.08);display:flex;align-items:center;justify-content:center;font-size:58px;font-weight:800;color:var(--blue);line-height:1;padding-top:24px}
.quote p{font-style:italic;font-size:13.5px;line-height:20px;color:#4c5a6a}
.who{position:absolute;left:0;bottom:0;display:flex;gap:16px;align-items:flex-start}
.avatar{width:54px;height:54px;background:linear-gradient(135deg,#c9a48a,#8b6e5a)}
.who b{display:block;font-size:13.5px;color:var(--navy);font-weight:600;margin-top:2px}
.who small{font-size:12px;color:#6f7c89}
/* tech */
.tech{position:absolute;top:2400px;left:94px;width:1012px;text-align:center}
.tech h2{font-size:27px}
.logos{display:flex;justify-content:space-between;align-items:center;margin-top:60px}
.logo{display:flex;align-items:center;gap:10px;font-size:28px;font-weight:600;color:var(--blue)}
.logo i{width:26px;height:26px;background:var(--blue);border-radius:50%}
/* footer */
.site-footer{position:absolute;top:2654px;left:0;width:1200px;height:356px;background:var(--footer);color:#dfe5ec;padding:82px 94px 0}
.foot-row{display:flex}
.foot-about{width:320px;font-size:12px;line-height:20px}
.socials{display:flex;gap:14px;margin-top:24px}
.socials span{width:20px;height:20px;border-radius:50%;background:#fff}
.foot-links{margin-left:361px;width:130px;font-size:12px}
.foot-links h4,.foot-contact h4{font-size:13px;color:#fff;font-weight:600;margin-bottom:20px;margin-top:-4px}
.foot-links li{list-style:none;margin-bottom:19px}
.foot-contact{font-size:12px;line-height:18px}
.foot-contact div{display:flex;gap:12px;margin-bottom:14px}
.foot-contact svg{flex:none;margin-top:3px}
.copy{position:absolute;left:94px;right:94px;bottom:0;border-top:1px solid #45566d;text-align:center;font-size:11.5px;padding:12px 0 10px;color:#c5ceda}
</style>
</head>
<body>
<div class="wrap">
<header class="site-header">
  <div class="brand"><span class="brand-dot"></span>Norvalith</div>
  <nav class="nav"><span>About Us</span><span>Services</span><span>Insights</span><span>Join Us</span><a class="btn-contact">Contact Us</a></nav>
</header>

<section class="hero">
  <div class="hero-photo" role="img" aria-label="Smiling support consultant wearing a headset in a bright office"></div>
  <div class="hero-body">
    <h1>Transformation <span class="y">Delivered</span></h1>
    <p>We do more for our customers than implement software. We listen. We work to understand where they are in their transformation journey and where they want to go. We partner with them to clear the roadblocks that stand in their way, ensuring they reach their destination. At <b>Norvalith</b>, we:</p>
    <ul class="ticks">
      <li>Focus on business value, with an emphasis on delivering value quickly.</li>
      <li>Meet our customers where they are without backing them up to the beginning of their journey.</li>
      <li>Provide a wide range of services, from strategy to product support.</li>
      <li>Commit to our customer’s long-term success.</li>
    </ul>
    <p style="margin-top:12px"><b>Norvalith</b> is business transformation, delivered.</p>
    <a class="btn-y" style="margin-top:42px">OUR STORY</a>
  </div>
</section>

<section class="services">
  <div class="services-top">
    <div>
      <h2>Transformation Supported by <span class="y">Technology</span></h2>
      <p>During our early years, <b>Norvalith</b> focused only on business transformation. We came to realize that successful transformation often depended on quality software implementations, and often more than one. Now we focus on five things, the five things most businesses need to reach their goals.</p>
    </div>
    <a class="btn-b">HOW WE WORK</a>
  </div>
  <div class="cards">
    <div class="card"><div class="card-icon"></div><h3>Business Transformation</h3></div>
    <div class="card active">
      <h3>ERP Implementations</h3>
      <p>Assess, upgrade, and implement ERP solutions to meet your needs.</p>
      <div class="learn">Learn More</div>
    </div>
    <div class="card"><div class="card-icon"></div><h3>CRM Implementations</h3></div>
    <div class="card"><div class="card-icon"></div><h3>BI and Data</h3></div>
    <div class="card"><div class="card-icon"></div><h3>Building the Right Team of People</h3></div>
  </div>
</section>

<section class="people">
  <div class="people-photo" role="img" aria-label="Team of five colleagues gathered around a wooden table with a laptop"></div>
  <div class="people-body">
    <h2>It’s the <span class="y">People</span></h2>
    <p>The world has changed in the past twenty years. The people you need might not all work for one company. Our clients want the best resources, available quickly. That’s why, in addition to our team of experts, we partner with:</p>
    <ul class="ticks">
      <li style="margin-bottom:6px">A large network of expert consultants who are the best at what they do</li>
      <li>Service providers all over the world to provide the resources and value that are right for you, available 24 × 7.</li>
    </ul>
    <p style="margin-top:10px;width:360px">People are invariably at the center of our customer’s success. Find out how we can add our experts to yours.</p>
    <a class="btn-y" style="margin-top:48px">OUR TEAM</a>
  </div>
</section>

<section class="clients">
  <div class="clients-top">
    <h2>What Our Clients <span class="y">Say</span></h2>
    <div class="arrows">
      <div class="arrow"><svg width="18" height="18" viewBox="0 0 18 18" fill="none" stroke="#8da0b4" stroke-width="2"><path d="M16 9H2M8 3L2 9l6 6"/></svg></div>
      <div class="arrow on"><svg width="18" height="18" viewBox="0 0 18 18" fill="none" stroke="#fff" stroke-width="2"><path d="M2 9h14M10 3l6 6-6 6"/></svg></div>
    </div>
  </div>
  <div class="quotes">
    <div class="quote"><div class="qmark">”</div><p>Lorem ipsum dolor sit amet consectetur. Lectus nec in vitae ornare scelerisque habitasse. Ut tristique quam amet a et. Sodales condimentum semper id turpis pretium morbi ultrices proin cursus. Suspendisse enim non viverra imperdiet.</p><div class="who"><div class="avatar" role="img" aria-label="Portrait of client"></div><div><b>Lena Whitford</b><small>Company Ipsum</small></div></div></div>
    <div class="quote"><div class="qmark">”</div><p>Lorem ipsum dolor sit amet consectetur. Lectus nec in vitae ornare scelerisque habitasse. Ut tristique quam amet a et. Sodales condimentum semper id turpis pretium morbi ultrices proin cursus. Suspendisse enim non viverra imperdiet.</p><div class="who"><div class="avatar" role="img" aria-label="Portrait of client" style="background:linear-gradient(180deg,#9fb4c6,#b39a7e)"></div><div><b>Aaron Jessup</b><small>Company Ipsum</small></div></div></div>
    <div class="quote"><div class="qmark">”</div><p>Lorem ipsum dolor sit amet consectetur. Lectus nec in vitae ornare scelerisque habitasse. Ut tristique quam amet a et. Sodales condimentum semper id turpis pretium morbi ultrices proin cursus. Suspendisse enim non viverra imperdiet.</p><div class="who"><div class="avatar" role="img" aria-label="Portrait of client" style="background:linear-gradient(135deg,#e9e9ea,#6b4b3a)"></div><div><b>Jonah Mercer</b><small>Company Ipsum</small></div></div></div>
  </div>
</section>

<section class="tech">
  <h2>Tech that We <span class="y">Use</span></h2>
  <div class="logos">
    <div class="logo"><i></i>Cloudora</div>
    <div class="logo"><i></i>Dynavista</div>
    <div class="logo"><i></i>Meshlink</div>
    <div class="logo"><i></i>Graphyte</div>
  </div>
</section>

<footer class="site-footer">
  <div class="foot-row">
    <div class="foot-about">
      <p>Many major projects fail to deliver anticipated benefits due to a few vital components. <b>Norvalith</b> specializes in these domains, bringing effectiveness, acceleration, and purpose to transformational initiatives. At <b>Norvalith</b>, our Industry Experts and experienced Technical Talent will bring Your Vision to reality on today’s Leading Platforms.</p>
      <div class="socials"><span aria-label="Social link 1"></span><span aria-label="Social link 2"></span><span aria-label="Social link 3"></span><span aria-label="Social link 4"></span></div>
    </div>
    <ul class="foot-links"><h4>Quick Links</h4><li>About Us</li><li>Services</li><li>Insights</li><li>Join Us</li></ul>
    <div class="foot-contact">
      <h4>Get in Touch</h4>
      <div><svg width="11" height="11" viewBox="0 0 12 12" fill="#5b8cc0"><path d="M2 0l3 3-1.5 2a8 8 0 0 0 3.5 3.5L9 7l3 3-2 2C5 12 0 7 0 2z"/></svg>(612) 555-0148</div>
      <div><svg width="11" height="11" viewBox="0 0 12 12" fill="#5b8cc0"><path d="M6 0a4 4 0 0 1 4 4c0 3-4 8-4 8S2 7 2 4a4 4 0 0 1 4-4z"/></svg>480 Harbor Point Suite 210,<br>Lakeview, MN 55410</div>
      <div><svg width="11" height="11" viewBox="0 0 12 12" fill="#5b8cc0"><path d="M0 2h12v8H0z"/></svg>hello@norvalith.example</div>
    </div>
  </div>
  <div class="copy">© 2023 Norvalith. All Rights Reserved.</div>
</footer>
</div>
</body>
</html>
```